I need a Facebook, Instagram post, for Outdoor Training
I need my logo,
Business name : Valmora Soccer Academy
Boys and girls Outdoor Soccer training
Passing, Kicking Shooting, Dribbling, Ball Control
Field: Brookvale Turf #5(1746 Hollowmere Lane Dunstead, MD 20419)
Time: 5:30pm-6:30pm 5-8 years old
6;30pm-7:30pm 9-12 years old
7:30pm-8:30pm 13-18 years old
Registration $210 ( Includes 1st month, registration, practice uniform)

Register online:
www.valmoraacademy.example
Phone:(240)555-0187

Target Market(s)

YOUTH KIDS

Colors
0054AA
0677BA
7BADD7
CADEEF
E8F1F8

Requirements
Must have
• blue , or black and white

```html
<!DOCTYPE html>
<html lang="en">
<head>
<meta charset="utf-8">
<title>Valmora Soccer Academy – Outdoor Training</title>
<link rel="stylesheet" href="https://fonts.googleapis.com/css2?family=Montserrat:ital,wght@0,400;0,500;0,700;0,800;1,600;1,700;1,900&display=swap">
<style>
  :root {
    --navy: #1a2b63;
    --yellow: #f7e400;
    --paper: #f4f4f4;
    --ink: #111111;
    --white: #ffffff;
  }
  * { margin: 0; padding: 0; box-sizing: border-box; }
  html, body { width: 1200px; height: 1200px; overflow: hidden; }
  body {
    background: var(--paper);
    font-family: "Montserrat", Arial, sans-serif;
    color: var(--ink);
  }
  .poster {
    position: relative;
    width: 1200px;
    height: 1200px;
    overflow: hidden;
    background: linear-gradient(135deg, #f7f7f7 0%, #eeeeee 50%, #f6f6f6 100%);
  }
  .art { position: absolute; inset: 0; }
  .brand-name {
    position: absolute;
    left: 72px;
    top: 96px;
    width: 230px;
    font-weight: 800;
    font-size: 36px;
    line-height: 1.12;
    color: var(--navy);
    text-transform: uppercase;
  }
  .audience {
    position: absolute;
    left: 66px;
    top: 360px;
    font-weight: 700;
    font-style: italic;
    font-size: 33px;
    color: var(--navy);
  }
  .headline {
    position: absolute;
    left: 64px;
    top: 398px;
    font-weight: 900;
    font-style: italic;
    font-size: 98px;
    line-height: 84px;
    color: var(--navy);
    letter-spacing: -1px;
    text-shadow: 4px 4px 0 var(--white), 5px 5px 0 var(--navy);
  }
  .skills {
    position: absolute;
    left: 65px;
    top: 592px;
    font-weight: 700;
    font-style: italic;
    font-size: 29px;
    color: var(--ink);
    letter-spacing: 0.3px;
  }
  .label {
    position: absolute;
    font-weight: 700;
    font-size: 29px;
    color: var(--navy);
  }
  .label-field { left: 68px; top: 676px; }
  .label-time { left: 68px; top: 846px; }
  .label-registration { left: 656px; top: 857px; }
  .venue-name {
    position: absolute;
    left: 69px;
    top: 718px;
    font-weight: 700;
    font-size: 28px;
  }
  .venue-address {
    position: absolute;
    left: 69px;
    top: 758px;
    font-weight: 400;
    font-size: 28px;
  }
  .schedule {
    position: absolute;
    left: 69px;
    top: 900px;
    font-size: 28px;
    font-weight: 400;
  }
  .schedule-row { display: flex; height: 51px; align-items: center; }
  .schedule-time { width: 240px; }
  .schedule-sep { width: 20px; color: var(--yellow); font-weight: 500; }
  .price {
    position: absolute;
    left: 658px;
    top: 918px;
    font-weight: 700;
    font-size: 29px;
  }
  .price-note {
    position: absolute;
    left: 656px;
    top: 960px;
    width: 520px;
    font-size: 29px;
    line-height: 39px;
  }
  .footer-cta {
    position: absolute;
    left: 65px;
    top: 1131px;
    font-weight: 700;
    font-size: 28px;
    color: var(--white);
  }
  .footer-url { color: var(--yellow); margin-left: 10px; }
  .footer-phone {
    position: absolute;
    left: 883px;
    top: 1129px;
    display: flex;
    align-items: center;
    gap: 12px;
    font-weight: 700;
    font-size: 29px;
    color: var(--navy);
  }
</style>
</head>
<body>
<main class="poster">
  <svg class="art" width="1200" height="1200" viewBox="0 0 1200 1200" aria-hidden="false">
    <defs>
      <linearGradient id="field-photo" x1="0" y1="0" x2="0" y2="1">
        <stop offset="0" stop-color="#f5f1e8"/>
        <stop offset="0.45" stop-color="#d9c9a4"/>
        <stop offset="0.7" stop-color="#c98a4e"/>
        <stop offset="1" stop-color="#6f9a34"/>
      </linearGradient>
      <radialGradient id="ball-fill" cx="0.4" cy="0.35" r="0.7">
        <stop offset="0" stop-color="#ffffff"/>
        <stop offset="0.7" stop-color="#d8d8d8"/>
        <stop offset="1" stop-color="#555555"/>
      </radialGradient>
    </defs>

    <polygon role="img" aria-label="Photo: young player in an orange kit shooting at goal on a sunny grass field with a goalkeeper in yellow"
      fill="url(#field-photo)"
      points="472,140 540,120 600,70 650,0 1200,0 1200,656 1120,645 1040,628 990,600 950,565 880,548 830,500 770,430 700,360 640,300 560,240 500,190"/>

    <polygon class="brush-band" fill="var(--yellow)"
      points="0,372 120,330 240,312 380,300 460,306 540,330 600,360 640,420 650,520 620,590 560,620 420,628 260,624 120,620 0,612"/>

    <rect x="55" y="682" width="126" height="28" fill="var(--yellow)"/>
    <rect x="55" y="852" width="126" height="28" fill="var(--yellow)"/>
    <rect x="652" y="862" width="230" height="30" fill="var(--yellow)"/>

    <g class="chevrons" fill="none" stroke="var(--navy)" stroke-width="11">
      <polyline points="430,58 450,79 430,100"/>
      <polyline points="464,58 484,79 464,100"/>
      <polyline points="498,58 518,79 498,100"/>
      <polyline points="532,58 552,79 532,100"/>
      <polyline points="566,58 586,79 566,100"/>
      <polyline points="600,58 620,79 600,100"/>
    </g>

    <circle role="img" aria-label="Illustration: black and white soccer ball" cx="736" cy="460" r="102" fill="url(#ball-fill)"/>

    <polygon class="footer-band" fill="var(--navy)" points="0,1096 854,1096 832,1200 0,1200"/>
    <polygon class="footer-phone-band" fill="var(--yellow)" points="854,1096 1200,1096 1200,1200 832,1200"/>
  </svg>

  <div class="brand-name">Valmora Soccer Academy</div>

  <div class="audience">BOYS AND GIRLS</div>
  <h1 class="headline">OUTDOOR<br>TRAINING</h1>
  <p class="skills">Passing | Kicking | Shooting | Dribbling | Ball Control</p>

  <div class="label label-field">Field</div>
  <div class="venue-name">Brookvale Turf #5</div>
  <div class="venue-address">1746 Hollowmere Lane Dunstead, MD 20419</div>

  <div class="label label-time">Time</div>
  <div class="schedule">
    <div class="schedule-row"><span class="schedule-time">5:30 - 6:30 pm</span><span class="schedule-sep">|</span><span>5-8 years old</span></div>
    <div class="schedule-row"><span class="schedule-time">6:30 - 7:30pm</span><span class="schedule-sep">|</span><span>9-12 years old</span></div>
    <div class="schedule-row"><span class="schedule-time">7:30 - 8:30pm</span><span class="schedule-sep">|</span><span>13-18 years old</span></div>
  </div>

  <div class="label label-registration">Registration</div>
  <div class="price">$210</div>
  <p class="price-note">Includes 1st month, registration, practice uniform</p>

  <div class="footer-cta">Register Online <span class="footer-url">www.valmoraacademy.example</span></div>
  <div class="footer-phone">
    <svg width="28" height="28" viewBox="0 0 24 24" aria-hidden="true">
      <path fill="var(--navy)" d="M6.6 10.8a15.1 15.1 0 0 0 6.6 6.6l2.2-2.2c.3-.3.7-.4 1-.2 1.1.4 2.3.6 3.6.6.6 0 1 .4 1 1V20c0 .6-.4 1-1 1A17 17 0 0 1 3 4c0-.6.4-1 1-1h3.5c.6 0 1 .4 1 1 0 1.3.2 2.5.6 3.6.1.3 0 .7-.2 1z"/>
    </svg>
    <span>(240)555-0187</span>
  </div>
</main>
</body>
</html>
```